【依頼目的/概要】
近日中に出版する予定の電子書籍(kindle版)の表紙デザインをお願いします。

【画像サイズ】
表紙ファイルの理想的な寸法は2560x1600ピクセルです。
注:画像の寸法は1000x625ピクセル以上であることが必要です。
画像の最大寸法は10000x10000ピクセルです。

【タイトル】
夜明けの庭で見つけた静かな暮らしの小さな習慣

【著者】
医師(循環器専門医、瑞穂橋文化振興会公認スポーツドクター)
桐原晴臣

【本の内容】
医師である私自身の実践したダイエット法について説明した本です。
ただ「食べるのガマンして体重が減りました」だけでは脂肪だけではなく、筋肉まで落ちてしまいます。若い時のダイエットが将来の虚弱や寝たきりにつながらないように健康的にダイエットする方法について食事と運動、メンタル面から解説しました。

*本文を参考資料として添付します。

【デザイン要望】
特にイメージはありませんので自由な発想でのデザインご応募楽しみにしています

*その他、必要な情報がありましたらお問い合わせください。

どの性別、どの年齢の人にも手に取ってもらいやすく、内容に関しても一見してわかりやすいデザインだと感じました。

どのデザインも甲乙つけがたく、大変悩みました。多数の方にご応募いただき、誠にありがとうございました。皆様とまたご縁がありましたらよろしくお願いいたします。今回は大変ありがとうございました。

```html
<!DOCTYPE html>
<html lang="ja">
<head>
<meta charset="utf-8">
<title>夜明けの庭で見つけた静かな暮らしの小さな習慣 表紙</title>
<link href="https://fonts.googleapis.com/css2?family=Noto+Sans+JP:wght@500;700;900&display=swap" rel="stylesheet">
<style>
  :root{
    --ink:#1a1a1a;
    --navy:#1f2a44;
    --red:#e0232b;
    --paper:#ffffff;
    --sand-light:#e9dccb;
    --sand:#d6bf9f;
    --sand-deep:#c4a880;
  }
  html,body{margin:0;padding:0;overflow:hidden;background:var(--paper);}
  .cover{
    position:relative;width:750px;height:1200px;overflow:hidden;
    background:var(--paper);
    font-family:"Noto Sans JP",sans-serif;color:var(--ink);
  }
  .vertical{writing-mode:vertical-rl;position:absolute;margin:0;line-height:1;font-weight:900;}
  .title{margin:0;}
  .title-line-1{right:25px;top:20px;font-size:92px;color:var(--ink);}
  .title-line-2{left:380px;top:50px;font-size:140px;color:var(--ink);}
  .title-aside{left:610px;top:600px;font-size:54px;color:var(--red);letter-spacing:2px;}
  .aside-bracket{position:absolute;left:580px;top:590px;}
  .title-line-3{left:240px;top:110px;font-size:135px;color:var(--red);}
  .title-line-4{left:30px;top:420px;font-size:140px;color:var(--red);}

  .gift{
    position:absolute;left:228px;top:665px;width:240px;
    text-align:center;font-weight:700;color:var(--ink);
  }
  .gift-label{
    display:inline-block;background:var(--red);color:#fff;
    font-size:20px;padding:4px 18px;border-radius:3px;margin-bottom:6px;
  }
  .gift-format{font-size:17px;margin:0 0 6px;}
  .gift-format span{display:inline-block;border:2px solid var(--ink);padding:0 8px;margin-right:6px;}
  .gift-format em{font-style:normal;color:var(--red);}
  .gift-item{font-size:19px;line-height:1.3;margin:0 0 4px;}
  .gift-item strong{display:block;color:var(--red);font-size:24px;font-weight:900;}

  .band{
    position:absolute;left:0;right:0;top:858px;bottom:0;
    background:linear-gradient(180deg,var(--sand-light),var(--sand) 60%,var(--sand-deep));
  }
  .portrait{
    position:absolute;left:440px;top:840px;width:310px;height:360px;
    background:radial-gradient(ellipse at 55% 45%,#f1f1f1 0%,#c9ccd2 55%,rgba(196,168,128,0) 80%);
  }
  .credential{
    right:18px;top:872px;height:250px;font-size:14px;font-weight:700;
    color:var(--navy);line-height:1.35;letter-spacing:0;
  }
  .author{right:70px;top:872px;font-size:44px;font-weight:900;color:var(--navy);}
  .author small{font-size:26px;margin-bottom:14px;display:inline-block;}

  .catch{
    position:absolute;left:380px;top:912px;width:250px;text-align:right;
    font-size:40px;font-weight:900;line-height:1.35;color:var(--navy);margin:0;
    text-shadow:0 0 6px #fff,0 0 6px #fff;
  }
  .catch .dots{text-emphasis:filled dot var(--navy);-webkit-text-emphasis:filled dot var(--navy);}
  .tagline{
    position:absolute;left:345px;top:1132px;margin:0;
    font-size:46px;font-weight:900;color:var(--navy);line-height:1.1;
    text-shadow:0 0 8px #fff,0 0 8px #fff;white-space:nowrap;
  }
</style>
</head>
<body>
<div class="cover">
  <div class="band"></div>
  <div class="portrait" role="img" aria-label="白衣姿で微笑む著者の写真"></div>

  <h1 class="title">
    <span class="vertical title-line-1">夜明けの庭で</span>
    <span class="vertical title-line-2">見つけた</span>
    <span class="vertical title-line-3">暮らしの</span>
    <span class="vertical title-line-4">小さな習慣</span>
    <span class="vertical title-aside">静かな</span>
  </h1>
  <svg class="aside-bracket" width="30" height="200" viewBox="0 0 30 200" aria-hidden="true">
    <path d="M24 4 Q6 4 8 50 Q10 92 2 100 Q10 108 8 150 Q6 196 24 196" fill="none" stroke="#e0232b" stroke-width="4"/>
  </svg>

  <div class="gift">
    <div class="gift-label">読者プレゼント</div>
    <p class="gift-format"><span>PDF冊子</span><em>無料</em></p>
    <p class="gift-item">「減量したい人は<br>是非食べて欲しい食品<strong>ベスト5」</strong></p>
    <p class="gift-item">「基礎代謝を上げる方法<strong>ベスト5」</strong></p>
  </div>

  <p class="vertical credential">循環器専門医<br>瑞穂橋文化振興会公認スポーツドクター</p>
  <p class="vertical author"><small>医師</small>桐原晴臣</p>

  <p class="catch">なりたい<br>自分になる<br><span class="dots">ために</span></p>
  <p class="tagline">健康的に痩せる。</p>
</div>
</body>
</html>
```